Electrical contractor

looking for a standard sized, horizontal, double sided business card for an electrical contractors business.
i have played around on microsoft word (only computer program i know how to use!) and will attach what i have made so far, really open to any ideas. i just want the ROFT to stand out to the rest of the business name.

i wish to use the colours black and green, and white for writing. i will attach the pictures i took off google, i want to either use them, or somethin similar for the back grounds

i wish the front to have the following info:
business name: R.O.F.T ELECTRICAL CONTRACTORS
MY NAME; DARREN HOLT
STATUS; A CLASS ELECTRICIAN
LICENSE NO; TRK784150
PH NO. 0437615942
EMAIL ADD. ROFT.ELECTRICAL@VOLTMAILBOX.COM
AND MY SLOGAN: where excellence meets integrity, and service comes with a smile.

i am not sure what to have on the back, other than what i do for work.eg titled WHAT WE DO
i dont want too much written on there or will look crowded, but options to add to back, from most important to least, please pick however many you think will look the best
new homes/extentions
led lighting and downlights
Solar Power
power
safety switches
switchboards
telephone and tv
smoke alarms
stoves and ovens
hot water systems
fault finding
re wiring
Updates

Thank you to those who have submitted designs, I would like to change my slogan to something more simple, I'm thinking something like. RELIABLE. EFFICIENT. PROFESSIONAL. AFFORDABLE. in what ever order you thinks fits best. Thanks

```html
<!DOCTYPE html>
<html lang="en">
<head>
<meta charset="utf-8">
<title>R.O.F.T Electrical Contractors – Business Card</title>
<link rel="stylesheet" href="https://fonts.googleapis.com/css2?family=Lato:wght@300;400;700&family=Federo&display=swap">
<style>
  :root {
    --stage: #1c1c1d;
    --card-black: #121212;
    --card-edge: #2a2a2a;
    --green-bright: #7dff5a;
    --green-mid: #2f9e2a;
    --green-deep: #0d3b12;
    --text-white: #ffffff;
    --text-soft: #e6e6e6;
  }
  * { margin: 0; padding: 0; box-sizing: border-box; }
  html, body {
    width: 1200px; height: 800px; overflow: hidden;
    background: var(--stage);
  }
  .stage { position: relative; width: 1200px; height: 800px; }
  .card {
    position: absolute; top: 241px;
    width: 520px; height: 318px;
    background: var(--card-black);
    border: 1px solid var(--card-edge);
    border-radius: 4px;
    overflow: hidden;
    color: var(--text-white);
    font-family: "Lato", sans-serif;
  }
  .card--back { left: 50px; }
  .card--front { left: 630px; }

  /* back side */
  .back-glow {
    position: absolute; left: 140px; top: 20px;
    width: 270px; height: 270px; border-radius: 50%;
    background: radial-gradient(circle at 50% 50%, rgba(90,190,80,0.55) 0%, rgba(40,110,40,0.45) 40%, rgba(13,59,18,0.35) 65%, rgba(18,18,18,0) 72%);
  }
  .slogan-intro {
    position: absolute; left: 0; right: 0; top: 36px;
    text-align: center;
    font-family: "Federo", sans-serif;
    font-size: 13px; letter-spacing: 1px; color: var(--text-soft);
  }
  .slogan {
    position: absolute; left: 20px; top: 78px; width: 480px;
    text-align: center; white-space: nowrap;
    font-family: "Federo", sans-serif;
    font-variant: small-caps;
    font-size: 16px; letter-spacing: 0.2px;
    transform: rotate(-8deg);
    transform-origin: 50% 50%;
  }
  .services {
    position: absolute; left: 0; right: 0; top: 120px;
    text-align: center;
  }
  .services-lead { font-size: 20px; font-weight: 300; }
  .services-list {
    list-style: none; margin-top: 10px;
    font-size: 14px; font-weight: 300; line-height: 1.35;
    color: var(--text-soft);
  }

  /* front side */
  .bulb-art {
    position: absolute; left: -20px; top: 120px;
    width: 300px; height: 230px;
    background: radial-gradient(ellipse at 30% 55%, var(--green-bright) 0%, #4fd23a 16%, var(--green-mid) 34%, var(--green-deep) 60%, rgba(18,18,18,0) 78%);
  }
  .front-content {
    position: absolute; right: 30px; top: 26px;
    text-align: right;
  }
  .company { font-size: 19px; font-weight: 700; letter-spacing: 0.3px; }
  .company-mark { color: var(--text-white); }
  .license { font-size: 10px; font-weight: 400; margin-top: 2px; color: var(--text-soft); }
  .holder-name { font-size: 17px; font-weight: 700; margin-top: 20px; }
  .holder-title { font-size: 14px; font-weight: 400; margin-top: 2px; }
  .contact {
    position: absolute; right: 30px; bottom: 30px;
    list-style: none; text-align: right;
    font-size: 15px; line-height: 1.45;
  }
  .contact-item { display: flex; justify-content: flex-end; align-items: center; gap: 8px; }
  .contact-item--icon-only { height: 16px; }
  .contact-item--email { margin-top: 4px; }
  .contact-icon { width: 13px; height: 13px; fill: var(--text-white); flex: none; }
</style>
</head>
<body>
<main class="stage">

  <section class="card card--back" aria-label="Card back">
    <div class="back-glow" role="img" aria-label="Green glowing light background image"></div>
    <p class="slogan-intro">MY SLOGAN IS</p>
    <p class="slogan">Where excellence meets integrity, and service comes with a smile</p>
    <div class="services">
      <p class="services-lead">led lighting and downlights</p>
      <ul class="services-list">
        <li>Solar Power / power</li>
        <li>safety switches / switchboards</li>
        <li>telephone and tv</li>
        <li>smoke alarms / stoves and ovens</li>
        <li>hot water systems</li>
        <li>fault finding / re wiring</li>
      </ul>
    </div>
  </section>

  <section class="card card--front" aria-label="Card front">
    <div class="bulb-art" role="img" aria-label="Glowing green light bulb with light rays"></div>
    <div class="front-content">
      <h1 class="company"><span class="company-mark">R.O.F.T</span> ELECTRICAL CONTRACTORS</h1>
      <p class="license">LICENSE NO; TRK784150</p>
      <p class="holder-name">DARREN HOLT</p>
      <p class="holder-title">A CLASS ELECTRICIAN</p>
    </div>
    <ul class="contact">
      <li class="contact-item">0437615942
        <svg class="contact-icon" viewBox="0 0 16 16" aria-hidden="true">
          <path d="M1 5c0-2 3-3 7-3s7 1 7 3v1h-4V5H5v1H1z"/>
          <path d="M3 8l2-2h6l2 2v6H3z"/>
        </svg>
      </li>
      <li class="contact-item contact-item--icon-only">
        <svg class="contact-icon" viewBox="0 0 16 16" aria-hidden="true">
          <path d="M1 3h14v10H1z"/>
          <path d="M1 3l7 6 7-6" fill="none" stroke="#121212" stroke-width="1.3"/>
        </svg>
      </li>
      <li class="contact-item contact-item--email">ROFT.ELECTRICAL@VOLTMAILBOX.COM</li>
    </ul>
  </section>

</main>
</body>
</html>
```